Harold Brisk Mechanical business cards

We need business cards designed for "Harold Brisk Mechanical" "Mechanical & Electrical Contractors" "Specializing in Service & Installation"
"Cooling, Heating, Service, Installations, Residential, Commercial"

```html
<!DOCTYPE html>
<html lang="en">
<head>
<meta charset="utf-8">
<title>Harold Brisk Mechanical – Business Cards</title>
<link rel="stylesheet" href="https://fonts.googleapis.com/css2?family=Montserrat:wght@600;700&family=Open+Sans:wght@400;600&display=swap">
<style>
  :root {
    --page: #d9d9d9;
    --card: #1b1b1c;
    --red: #e8262f;
    --white: #f4f4f4;
    --grey: #9a9a9a;
    --rule: #8a8a8a;
  }
  * { box-sizing: border-box; margin: 0; padding: 0; }
  html, body { width: 1200px; height: 900px; overflow: hidden; }
  body {
    background: var(--page);
    font-family: "Open Sans", sans-serif;
    color: var(--white);
    display: flex;
    flex-direction: column;
    align-items: center;
    justify-content: center;
    gap: 50px;
  }
  .card {
    position: relative;
    width: 700px;
    height: 400px;
    background: var(--card);
    box-shadow: 0 10px 30px rgba(0,0,0,.25);
    overflow: hidden;
  }
  .card--front { height: 380px; }

  /* front */
  .brand {
    display: flex;
    align-items: center;
    gap: 12px;
    font-family: "Open Sans", sans-serif;
    font-weight: 600;
  }
  .brand__square { width: 22px; height: 22px; background: var(--red); flex: none; }
  .brand--front { position: absolute; top: 52px; right: 50px; font-size: 22px; color: var(--white); }
  .divider {
    position: absolute;
    left: 50px; right: 50px;
    top: 206px;
    height: 1px;
    background: var(--rule);
  }
  .person { position: absolute; left: 50px; top: 124px; }
  .person__name {
    font-family: "Montserrat", sans-serif;
    font-weight: 700;
    font-size: 34px;
    color: var(--red);
    line-height: 1.1;
  }
  .person__role { font-size: 17px; margin-top: 6px; }
  .contacts {
    position: absolute; left: 50px; top: 236px;
    list-style: none;
    font-size: 17px;
    line-height: 1.75;
  }
  .contacts li { display: flex; align-items: center; gap: 12px; }
  .contacts svg { width: 14px; height: 14px; fill: var(--red); flex: none; }
  .contacts .accent { color: var(--red); }
  .address {
    position: absolute; right: 50px; top: 240px;
    text-align: right;
    font-size: 17px;
    line-height: 1.5;
  }

  /* back */
  .brand--back {
    position: absolute;
    top: 110px; left: 0; right: 0;
    justify-content: center;
    font-size: 34px;
    color: var(--grey);
  }
  .brand--back .brand__square { width: 34px; height: 34px; background: var(--grey); }
  .tagline {
    position: absolute;
    left: 0; right: 0; top: 235px;
    text-align: center;
    font-size: 19px;
    line-height: 1.5;
  }
</style>
</head>
<body>

  <section class="card card--front" aria-label="Business card front">
    <div class="brand brand--front">
      <span class="brand__square"></span>
      <span>Harold Brisk Mechanical</span>
    </div>

    <div class="person">
      <h1 class="person__name">Daniel Reeves</h1>
      <p class="person__role">Managing Partner</p>
    </div>

    <div class="divider"></div>

    <ul class="contacts">
      <li>
        <svg viewBox="0 0 24 24" aria-hidden="true"><path d="M6.6 10.8a15.1 15.1 0 0 0 6.6 6.6l2.2-2.2c.3-.3.7-.4 1-.2 1.1.4 2.3.6 3.6.6.6 0 1 .4 1 1V20c0 .6-.4 1-1 1A17 17 0 0 1 3 4c0-.6.4-1 1-1h3.5c.6 0 1 .4 1 1 0 1.3.2 2.5.6 3.6.1.3 0 .7-.2 1z"/></svg>
        <span>915-555-0142</span>
      </li>
      <li>
        <svg viewBox="0 0 24 24" aria-hidden="true"><path d="M2 5h20v14H2zm2 2v.5l8 5 8-5V7zm0 2.8V17h16V9.8l-8 5z"/></svg>
        <span>info@haroldbrisk.com</span>
      </li>
      <li>
        <svg viewBox="0 0 24 24" aria-hidden="true"><path d="M12 2a10 10 0 1 0 0 20 10 10 0 0 0 0-20zm6.9 9h-3a15 15 0 0 0-1.3-5.6A8 8 0 0 1 18.9 11zM12 4.1c.9 1.3 1.8 3.7 1.9 6.9h-3.8c.1-3.2 1-5.6 1.9-6.9zM9.4 5.4A15 15 0 0 0 8.1 11h-3a8 8 0 0 1 4.3-5.6zM5.1 13h3a15 15 0 0 0 1.3 5.6A8 8 0 0 1 5.1 13zm6.9 6.9c-.9-1.3-1.8-3.7-1.9-6.9h3.8c-.1 3.2-1 5.6-1.9 6.9zm2.6-1.3a15 15 0 0 0 1.3-5.6h3a8 8 0 0 1-4.3 5.6z"/></svg>
        <span>www.<span class="accent">haroldbrisk</span>.com</span>
      </li>
    </ul>

    <address class="address" style="font-style:normal">
      2817 Larkspur Lane<br>
      Fairview, TN 38120
    </address>
  </section>

  <section class="card card--back" aria-label="Business card back">
    <div class="brand brand--back">
      <span class="brand__square"></span>
      <span>Harold Brisk Mechanical</span>
    </div>

    <p class="tagline">
      Harold Brisk Mechanical<br>
      Mechanical &amp; Electrical Contractors - Specializing in Service &amp; Installation<br>
      Cooling - Heating - Service - Installations - Residential - Commercial
    </p>
  </section>

</body>
</html>
```